small business focused on life coaching and helping others "create better tomorrows" needs a website

The Pax T Group needs a website that focuses on life coaching and helping others "create better tomorrows"; This is a sole proprietorship so the focus should be on Marla, who has worn many hats and in an excellent position to help others. It should include 6 pages _ Home, Bio, Services, Book, Media, Contact Us and the logo that was created by Lumo Forge; also include testimonials from 5-6 individuals as well as why one might need these services (see file included)

Target Market(s)

Immigrants who need help navigating American system in the workplace, home or community, immigrant or at-risk students unable to communicate with their immigrant parents (due to language or unfamiliarity with the new culture) but would share with someone they trust, those in need of a mentor or help with career advancement or choices, those in need of help with public speaking or leadership development - Marla is someone who has worn many hats and in a position to help - extensive networking, an immigrant herself, former teacher, community leader, TV talk show host, author, mother, grandmother, etc.

Industry/Entity Type

Business

Coding

Coded - Design and coding required

Number of Pages Required

5+ page

Font styles to use
Sans Serif

Colors
cadf82
add136

Requirements
Must have
• visuals of Marla - present image of competency, caring, professionalism; need to include a 30-second video (in process of being produced) of Marla promoting the services, need to include 5-6 testimonials (which will be sent later). Please see the document that describes the different pages of the website and what should be included. Give the image of Marla's ability to help people GROW into a more productive self
Nice to have
• This is a sole proprietor business and as such, need to have people feel comfortable in who I am - trust is critical and that is why experience and competency should be shown

```html
<!DOCTYPE html>
<html lang="en">
<head>
<meta charset="utf-8">
<title>The Pax T Group – Building Brighter Futures</title>
<link rel="stylesheet" href="https://fonts.googleapis.com/css2?family=Open+Sans:wght@400;600;700&family=Montserrat:wght@400;500&display=swap">
<style>
  :root {
    --green: #add136;
    --green-light: #cadf82;
    --green-dark: #6f8a1e;
    --ink: #1a1a1a;
    --text: #3b3b3b;
    --muted: #8a8a8a;
    --line: #cfcfcf;
    --bar: #000000;
    --white: #ffffff;
    --pale: #f1f1f1;
  }
  * { margin: 0; padding: 0; box-sizing: border-box; }
  html, body { width: 1200px; height: 2564px; overflow: hidden; }
  body { position: relative; background: var(--white); font-family: "Open Sans", Arial, sans-serif; color: var(--text); }
  .abs { position: absolute; }

  /* Header */
  .site-header { position: absolute; left: 0; top: 0; width: 1200px; height: 60px; background: var(--bar); z-index: 5; }
  .brand { position: absolute; left: 99px; top: 10px; color: var(--white); }
  .brand-name { font-size: 16px; font-weight: 600; line-height: 20px; }
  .brand-tagline { font-size: 11px; font-weight: 400; line-height: 14px; }
  .main-nav a { position: absolute; top: 20px; color: var(--white); font-size: 13px; text-decoration: none; font-weight: 400; }
  .main-nav a.active { padding-bottom: 4px; border-bottom: 2px solid var(--green); }

  /* Hero */
  .hero { position: absolute; left: 0; top: 60px; width: 1200px; height: 624px;
    background: linear-gradient(100deg, #5b5652 0%, #7b726b 30%, #8d8178 55%, #6a605a 80%, #4d4743 100%); }
  .hero-shade { position: absolute; inset: 0; background: linear-gradient(90deg, rgba(0,0,0,.35) 0%, rgba(0,0,0,0) 55%); }
  .hero-title { position: absolute; left: 99px; top: 112px; color: var(--white); font-size: 40px; font-weight: 700; letter-spacing: .5px; }
  .hero-text { position: absolute; left: 99px; top: 183px; width: 500px; color: var(--white); font-size: 21px; font-weight: 700; line-height: 26px; }
  .hero-text p + p { margin-top: 24px; }
  .btn-outline { position: absolute; left: 99px; top: 322px; width: 145px; height: 36px; border: 1.5px solid var(--white);
    color: var(--white); font-size: 16px; font-weight: 600; text-align: center; line-height: 33px; }
  .hero-dots span { position: absolute; left: 1086px; width: 12px; height: 12px; border-radius: 50%; border: 2px solid var(--white); }
  .hero-dots span.on { background: var(--white); }

  /* Special areas */
  .section-title { position: absolute; left: 0; width: 1200px; text-align: center; font-size: 24px; font-weight: 400; color: var(--green); }
  .section-title span { display: inline-block; padding-bottom: 4px; border-bottom: 1px solid var(--green); }
  .area { position: absolute; top: 802px; width: 320px; }
  .area-icon { position: absolute; left: 0; top: 0; width: 34px; height: 34px; border-radius: 50%; border: 1.5px solid var(--green); }
  .area-icon svg { position: absolute; left: 7px; top: 7px; }
  .area h3 { position: absolute; left: 51px; top: 2px; font-size: 17px; font-weight: 600; color: var(--ink); white-space: nowrap; }
  .area p { position: absolute; left: 51px; top: 36px; width: 255px; font-size: 13px; line-height: 20.5px; color: var(--muted); }
  .pager span { position: absolute; top: 946px; width: 12px; height: 12px; border-radius: 50%; border: 1px solid #d8d8d8; }
  .pager span.on { background: #0f1d33; border-color: #0f1d33; }

  /* Questions band */
  .needs { position: absolute; left: 0; top: 1013px; width: 1200px; height: 423px;
    background: linear-gradient(90deg, var(--green) 0%, #b6d64c 50%, var(--green) 100%); }
  .needs-list { position: absolute; left: 100px; top: 45px; width: 560px; list-style: none; }
  .needs-list li { position: relative; padding-left: 44px; font-size: 13.5px; line-height: 20px; color: var(--ink); margin-bottom: 21px; }
  .needs-list li::before { content: ""; position: absolute; left: 2px; top: 4px; width: 9px; height: 9px; background: var(--white); transform: rotate(45deg); }
  .needs-list li.two { margin-bottom: 19px; }
  .media-back { position: absolute; left: 870px; top: 52px; width: 231px; height: 229px; background: linear-gradient(160deg, #d9d3c8, #8f8a6a 60%, #6b6a4c); border: 1px solid #ffffff80; }
  .media-front { position: absolute; left: 701px; top: 137px; width: 229px; height: 231px; background: linear-gradient(160deg, #6d5f57, #9a8c7d 55%, #4e4540); border: 1px solid #ffffff80; }
  .play { position: absolute; left: 794px; top: 284px; width: 44px; height: 44px; border-radius: 50%; border: 2px solid var(--white); background: rgba(0,0,0,.25); }
  .play svg { position: absolute; left: 15px; top: 11px; }

  /* Business */
  .photo { position: absolute; width: 233px; height: 123px; }
  .business-title { position: absolute; left: 612px; top: 1484px; font-size: 24px; color: var(--green); font-weight: 600; padding-bottom: 4px; border-bottom: 1px solid var(--green); }
  .business-text { position: absolute; left: 612px; top: 1556px; width: 490px; font-family: "Montserrat", Arial, sans-serif; font-size: 12px; line-height: 20.6px; color: var(--text); }

  /* Testimonials */
  .testimonials { position: absolute; left: 0; top: 1806px; width: 1200px; height: 351px; background: var(--green); }
  .testimonials-title { position: absolute; left: 0; top: 45px; width: 1200px; text-align: center; font-size: 24px; font-weight: 600; color: var(--ink); }
  .testimonials-title span { display: inline-block; padding-bottom: 4px; border-bottom: 1px solid var(--ink); }
  .quote-frame { position: absolute; left: 159px; top: 117px; }
  .quote-text { position: absolute; left: 180px; top: 152px; width: 840px; text-align: center; font-size: 13.5px; line-height: 21px; color: var(--ink); }
  .quote-author { position: absolute; left: 0; top: 249px; width: 1200px; text-align: center; color: var(--white); font-size: 15px; font-weight: 600; }
  .quote-author::before { content: ""; display: inline-block; width: 52px; height: 1px; background: var(--white); vertical-align: middle; margin-right: 12px; }
  .arrow { position: absolute; top: 190px; width: 38px; height: 38px; background: var(--green-dark); }
  .arrow svg { position: absolute; left: 12px; top: 11px; }

  /* Contact */
  .contact-heading { position: absolute; top: 2203px; font-size: 20px; font-weight: 400; color: #333; }
  .contact-details { position: absolute; left: 99px; top: 2256px; font-size: 13px; line-height: 21px; color: #555; }
  .field { position: absolute; border-bottom: 1px solid var(--line); height: 36px; font-size: 12px; color: #9b9b9b; padding-top: 4px; }
  .btn-send { position: absolute; left: 870px; top: 2446px; width: 145px; height: 36px; background: linear-gradient(#86b63a, #5e8f1f);
    color: var(--white); font-size: 13px; line-height: 36px; padding-left: 45px; }
  .btn-send svg { position: absolute; left: 15px; top: 11px; }
  .social span { position: absolute; left: 1080px; width: 18px; height: 18px; border-radius: 50%; background: #9a9a9a; }

  .site-footer { position: absolute; left: 0; top: 2529px; width: 1200px; height: 35px; background: var(--bar); color: var(--white);
    text-align: center; font-size: 12px; line-height: 35px; }
</style>
</head>
<body>

<header class="site-header">
  <div class="brand">
    <div class="brand-name">The Pax T Group</div>
    <div class="brand-tagline">Building Brighter Futures</div>
  </div>
  <nav class="main-nav">
    <a class="active" href="#" style="left:523px">Home</a>
    <a href="#" style="left:628px">Bio</a>
    <a href="#" style="left:714px">Services</a>
    <a href="#" style="left:831px">Book</a>
    <a href="#" style="left:929px">Media</a>
    <a href="#" style="left:1035px">Contact Us</a>
  </nav>
</header>

<section class="hero" role="img" aria-label="Photo of Marla smiling beside a colleague in a hat at a conference">
  <div class="hero-shade"></div>
  <h1 class="hero-title">WHAT YOU DO</h1>
  <div class="hero-text">
    <p>Tell customers more about you.</p>
    <p>Add a few words and a stunning pic to grab their attention and get them to click.</p>
  </div>
  <div class="btn-outline">Read More</div>
  <div class="hero-dots">
    <span class="on" style="top:139px"></span>
    <span style="top:178px"></span>
    <span style="top:216px"></span>
  </div>
</section>

<svg class="abs" style="left:0;top:684px" width="1200" height="329" aria-hidden="true">
  <polygon points="0,140 0,329 110,329" fill="var(--pale)"/>
</svg>

<h2 class="section-title" style="top:728px"><span>SPECIAL AREAS</span></h2>

<div class="area" style="left:108px">
  <div class="area-icon"><svg width="18" height="18" viewBox="0 0 18 18"><path d="M4 14 L14 4 M9 4 h5 v5" stroke="#add136" stroke-width="1.8" fill="none"/></svg></div>
  <h3>Careers</h3>
  <p>Sed ut perspiciatis unde omnis iste natus error sit voluptatem accusantium dolo&shy;remque laudantium, totam rem aperiam,</p>
</div>
<div class="area" style="left:453px">
  <div class="area-icon"><svg width="18" height="18" viewBox="0 0 18 18"><path d="M3 15 L5 10 L12 3 L15 6 L8 13 Z" stroke="#add136" stroke-width="1.6" fill="none"/></svg></div>
  <h3>Acculturation</h3>
  <p>Sed ut perspiciatis unde omnis iste natus error sit voluptatem accusantium dolo&shy;remque laudantium, totam rem aperiam,</p>
</div>
<div class="area" style="left:797px">
  <div class="area-icon"><svg width="18" height="18" viewBox="0 0 18 18"><path d="M3 7 h4 l7 -4 v12 l-7 -4 h-4 Z" stroke="#add136" stroke-width="1.6" fill="none"/></svg></div>
  <h3>Leadership Development</h3>
  <p>Sed ut perspiciatis unde omnis iste natus error sit voluptatem accusantium dolo&shy;remque laudantium, totam rem aperiam,</p>
</div>

<div class="pager">
  <span class="on" style="left:556px"></span>
  <span style="left:594px"></span>
  <span style="left:632px"></span>
</div>

<section class="needs">
  <ul class="needs-list">
    <li>Are you an immigrant needing help navigating the American system?</li>
    <li class="two">Are you an immigrant parent unable to support your children's career choice or life issue</li>
    <li>Do you need help with your job search?</li>
    <li>Are you considering a career change?</li>
    <li>Are you struggling to balance demands of work, home and life?</li>
    <li>Do you need help with time management, leadership development, etc.?</li>
    <li>Are you worried about your teenager's change in behavior?</li>
    <li>Is your family struggling with an addiction/mental health issue?</li>
  </ul>
  <div class="media-back" role="img" aria-label="Photo of Marla with two women holding award plaques"></div>
  <div class="media-front" role="img" aria-label="Video still of Marla receiving an award with two men"></div>
  <div class="play"><svg width="14" height="18" viewBox="0 0 14 18"><path d="M0 0 L14 9 L0 18 Z" fill="#fff"/></svg></div>
</section>

<svg class="abs" style="left:0;top:1436px" width="1200" height="370" aria-hidden="true">
  <polygon points="0,0 110,0 0,130" fill="var(--pale)"/>
  <polygon points="1030,0 1200,0 1200,130" fill="var(--pale)"/>
</svg>

<div class="photo" style="left:97px;top:1492px;background:linear-gradient(160deg,#2e2230,#6f5a73 55%,#3a2d3e)" role="img" aria-label="Photo of Marla seated with family members on a stage"></div>
<div class="photo" style="left:355px;top:1492px;background:linear-gradient(160deg,#3c332a,#8d8560 55%,#4a4133)" role="img" aria-label="Photo of Marla with two women at an event"></div>
<div class="photo" style="left:97px;top:1632px;background:linear-gradient(160deg,#7a3a2c,#a45b4b 50%,#2e2a33)" role="img" aria-label="Photo of Marla with two guests at a gala"></div>
<div class="photo" style="left:355px;top:1632px;background:linear-gradient(160deg,#4a2a24,#8a6a5a 55%,#2c2320)" role="img" aria-label="Photo of Marla receiving an award with two men"></div>

<h2 class="business-title">BUSINESS</h2>
<p class="business-text">Life coach (this is a business that is focused on the individual – Marla Reyes. As such, need to present Marla as a mature professional with extensive expe&shy;rience in working with people and someone who has been very effective in getting things done. Aside from her personal experience as an immigrant, parent and grandparent, Marla has decades of experience as a teacher and administrator in a number of school systems, Director of a countywide agency, community leader heading a national organization with chapters nationally, talk show host, public speaker/facilitator/emcee, human resource administrator responsive for recruitment and compliance issues, board member for numerous commissions and organizations, etc.</p>

<section class="testimonials">
  <h2 class="testimonials-title"><span>TESTMONIALS</span></h2>
  <svg class="quote-frame" width="882" height="182" viewBox="0 0 882 182" aria-hidden="true">
    <path d="M100 2 H880 V180 H775 M715 180 H2 V2 H40" fill="none" stroke="#fff" stroke-width="3"/>
    <text x="70" y="46" text-anchor="middle" fill="#fff" font-family="Open Sans, sans-serif" font-size="64" font-weight="700">&#8220;</text>
    <text x="745" y="224" text-anchor="middle" fill="#fff" font-family="Open Sans, sans-serif" font-size="64" font-weight="700">&#8221;</text>
  </svg>
  <p class="quote-text">Marla is my "go-to" person for just about anything. She has been a significant support in my acculturation into western/American culture - helping me navigate the many aspects of life's journey. Through her guidance, I have gained much confidence in myself and in my approach to resolving issues. Her immigrant experience helps her understand my challenges. I cannot thank her enough for alway being there whenever I have needed guidance.</p>
  <div class="quote-author">Nora K.</div>
  <div class="arrow" style="left:106px"><svg width="14" height="16" viewBox="0 0 14 16"><path d="M10 2 L4 8 L10 14" stroke="#fff" stroke-width="2.5" fill="none"/></svg></div>
  <div class="arrow" style="left:1056px"><svg width="14" height="16" viewBox="0 0 14 16"><path d="M4 2 L10 8 L4 14" stroke="#fff" stroke-width="2.5" fill="none"/></svg></div>
</section>

<h2 class="contact-heading" style="left:99px">CONTACT ME</h2>
<div class="contact-details">
  418 Alder Lane, 5520,<br>
  Fairview. United States.<br>
  555-014-2290<br>
  marla.reyes@paxmail.net<br>
  https://www.thepaxtgroup.com
</div>

<h2 class="contact-heading" style="left:355px">DROP ME A LINE</h2>
<div class="field" style="left:355px;top:2259px;width:317px">Name</div>
<div class="field" style="left:699px;top:2259px;width:316px">Email</div>
<div class="field" style="left:355px;top:2328px;width:660px">Subject</div>
<div class="field" style="left:355px;top:2395px;width:660px">Message</div>
<div class="btn-send"><svg width="20" height="14" viewBox="0 0 20 14"><rect x="1" y="1" width="18" height="12" fill="none" stroke="#fff" stroke-width="1.5"/><path d="M1 1 L10 8 L19 1" fill="none" stroke="#fff" stroke-width="1.5"/></svg>Send message</div>

<div class="social" aria-hidden="true">
  <span style="top:2215px"></span>
  <span style="top:2255px"></span>
  <span style="top:2296px"></span>
  <span style="top:2337px"></span>
</div>

<footer class="site-footer">Copyright The Pax T Group © 2017 - | All Rights Reserved</footer>

</body>
</html>
```